Marvia Quenby Business Cards

We Need two Business Cards with bleeds. the only difference between the two cards is the backaround color one lilac and pink. Attached we have the cards please match up the logo's and text. Take out the orange box out.

Target Market(s)

double-sided business cards

Industry/Entity Type

Business

Logo Text

match up as best as possible

Colors
f59195
d2a4cc

Requirements
Must have
• n/a
Nice to have
• n/a
Should not have
• n/a

```html
<!DOCTYPE html>
<html lang="en">
<head>
<meta charset="utf-8">
<title>Marvia Quenby-Hale MD – Business Cards</title>
<link rel="stylesheet" href="https://fonts.googleapis.com/css2?family=Montserrat:ital,wght@0,300;0,400;0,500;1,300&family=Great+Vibes&display=swap">
<style>
  :root {
    --page-bg: #efeeec;
    --pink: #f59195;
    --lilac: #d2a4cc;
    --white: #ffffff;
    --text-soft: rgba(255,255,255,0.95);
    --sans: "Montserrat", Arial, sans-serif;
    --script: "Great Vibes", cursive;
  }
  * { margin: 0; padding: 0; box-sizing: border-box; }
  html, body { width: 1200px; height: 1000px; overflow: hidden; }
  body { background: var(--page-bg); position: relative; font-family: var(--sans); color: var(--white); }

  .card { position: absolute; width: 620px; height: 357px; }
  .card--pink { left: 132px; top: 136px; background: var(--pink); }
  .card--lilac { left: 423px; top: 541px; background: var(--lilac); }

  .heading { position: absolute; left: 200px; width: 398px; text-align: center; }
  .doctor-name { font-weight: 500; font-size: 26px; letter-spacing: 0.2px; position: absolute; left: 0; right: 0; top: 46px; }
  .credential { font-weight: 300; font-size: 17px; position: absolute; left: 0; right: 0; top: 84px; }
  .specialty { font-weight: 300; font-size: 17px; position: absolute; left: 0; right: 0; top: 111px; letter-spacing: 0.3px; }
  .specialty--script { font-family: var(--script); font-size: 27px; top: 116px; letter-spacing: 0; }
  .availability { font-weight: 300; font-size: 14px; position: absolute; left: 0; right: 0; top: 147px; }
  .card--lilac .availability { top: 156px; }

  .services { position: absolute; left: 58px; list-style: none; font-weight: 300; font-style: italic; }
  .card--pink .services { top: 214px; font-size: 16px; line-height: 30px; }
  .card--lilac .services { top: 215px; font-size: 15px; line-height: 22px; }

  .contact { position: absolute; left: 298px; list-style: none; font-weight: 300; font-size: 14px; }
  .contact li { display: flex; align-items: center; height: 30px; }
  .contact .icon { width: 18px; height: 14px; margin-right: 16px; flex: none; }
  .card--pink .contact { top: 209px; }
  .card--lilac .contact { top: 188px; }
  .card--lilac .contact li.line { height: 24px; }

  .brand { position: absolute; display: flex; align-items: center; gap: 10px; }
  .brand-dot { width: 112px; height: 112px; border-radius: 50%; background: var(--white); display: flex; align-items: center; justify-content: center; text-align: center; }
  .brand-name { font-weight: 500; font-size: 15px; line-height: 19px; color: var(--pink); }
  .card--pink .brand { left: 52px; top: 52px; }
  .card--lilac .brand { left: 48px; top: 60px; flex-direction: column; gap: 10px; }
  .brand-ring { width: 26px; height: 26px; border-radius: 50%; border: 3px solid var(--white); }
  .card--lilac .brand-name { color: var(--white); font-size: 17px; line-height: 22px; text-align: center; }
</style>
</head>
<body>

<section class="card card--pink">
  <div class="brand">
    <div class="brand-dot"><span class="brand-name">Marvia<br>Quenby</span></div>
  </div>
  <div class="heading">
    <h1 class="doctor-name">Marvia Quenby-Hale MD</h1>
    <p class="credential">Board Certified</p>
    <p class="specialty">Women’s Health &amp; Wellness Specialist</p>
    <p class="availability">By Appointment</p>
  </div>
  <ul class="services">
    <li>Obstetrics</li><li>Gynecology</li><li>Family Planning</li><li>Menopause</li>
  </ul>
  <ul class="contact">
    <li>418 Birchwood Road, Fairmont NY 11090</li>
    <li><svg class="icon" viewBox="0 0 18 14"><path d="M1 5c0-3 16-3 16 0v1h-4V4H5v2H1z M4 7h10l2 6H2z" fill="#fff"/></svg>555.210.4418/4419</li>
    <li><svg class="icon" viewBox="0 0 18 14"><rect x="5" y="0" width="8" height="4" fill="#fff"/><rect x="1" y="5" width="16" height="6" rx="1" fill="#fff"/><rect x="5" y="9" width="8" height="5" fill="#fff"/></svg>555.210.4453</li>
    <li><svg class="icon" viewBox="0 0 18 14"><rect x="1" y="2" width="16" height="11" fill="#fff"/><path d="M1 2l8 6 8-6" fill="none" stroke="var(--pink)" stroke-width="1.3"/></svg>q-hale@mailbox.net</li>
  </ul>
</section>

<section class="card card--lilac">
  <div class="brand">
    <span class="brand-ring"></span>
    <span class="brand-name">Marvia<br>Quenby</span>
  </div>
  <div class="heading">
    <h1 class="doctor-name">Marvia Quenby-Hale MD</h1>
    <p class="credential">Board Certified</p>
    <p class="specialty specialty--script">Women’s Health &amp; Wellness Specialist</p>
    <p class="availability">By Appointment</p>
  </div>
  <ul class="services">
    <li>Obstetrics</li><li>Gynecology</li><li>Family Planning</li><li>Weight Management</li><li>Menopause</li>
  </ul>
  <ul class="contact">
    <li class="line">207-14 Maplecrest Parkway</li>
    <li class="line">Maplecrest, New York 11490</li>
    <li><svg class="icon" viewBox="0 0 18 14"><path d="M1 5c0-3 16-3 16 0v1h-4V4H5v2H1z M4 7h10l2 6H2z" fill="#fff"/></svg>555.318.7125</li>
    <li><svg class="icon" viewBox="0 0 18 14"><rect x="5" y="0" width="8" height="4" fill="#fff"/><rect x="1" y="5" width="16" height="6" rx="1" fill="#fff"/><rect x="5" y="9" width="8" height="5" fill="#fff"/></svg>555.318.7126</li>
    <li><svg class="icon" viewBox="0 0 18 14"><rect x="1" y="2" width="16" height="11" fill="#fff"/><path d="M1 2l8 6 8-6" fill="none" stroke="var(--lilac)" stroke-width="1.3"/></svg>q-hale@mailbox.net</li>
  </ul>
</section>

</body>
</html>
```